We need a logo and landing page designed. We are a full-service general contractor based in Tempe Arizona. We can provide all phases of construction from design to completion. We specialize in commercial and residential remodels, as well as ground-up construction. We will like to see designs that primarily used reds, blues, blacks, whites, etc. The design should be a professional yet fun, easy-to-read format. Our name is Oak Ledger Construction...I would like to see some designs that incorporate a "oak ledger" and some without.
The final design should communicate a professional, quality-driven, safety oriented full service business.

Target Market(s)

Building owners, land developers, homeowners

Industry/Entity Type

Commercial Construction

Coding

Coded - Design and coding required

Number of Pages Required

1 page

Font styles to use
Serif

Colors
0054AA
0677BA
7BADD7
CADEEF
E8F1F8
59FF00
82FF00
B8FF75
E3FFCB
F4FFEA
EE7325
F08F49
F5BC92
FAE3D3
FDF4ED
EB3D1F
EC4F4E
F09395
F8D3D4
FCEDEE

```html
<!DOCTYPE html>
<html lang="en">
<head>
<meta charset="utf-8">
<title>Oak Ledger Construction</title>
<link href="https://fonts.googleapis.com/css2?family=Playfair+Display:wght@700&family=Rajdhani:wght@600;700&family=Mulish:wght@400;600&display=swap" rel="stylesheet">
<style>
:root{
  --navy:#0f2d4d;
  --blue:#0054AA;
  --blue-mid:#0677BA;
  --blue-light:#7BADD7;
  --blue-pale:#E8F1F8;
  --green:#59FF00;
  --green-dk:#5fb80a;
  --orange:#EE7325;
  --orange-lt:#F08F49;
  --peach:#FAE3D3;
  --red:#EB3D1F;
  --red-lt:#EC4F4E;
  --ink:#141414;
  --text:#2a2a2a;
  --footer:#161616;
  --white:#ffffff;
}
*{margin:0;padding:0;box-sizing:border-box}
html,body{width:1200px;height:3407px;overflow:hidden;background:#fff}
body{position:relative;font-family:"Mulish",sans-serif;color:var(--text)}
.abs{position:absolute}
.serif{font-family:"Playfair Display",serif;font-weight:700;color:var(--ink)}
.btn{position:absolute;background:var(--red);color:#fff;font-family:"Mulish",sans-serif;font-size:11px;font-weight:600;text-transform:uppercase;display:flex;align-items:center;justify-content:center;border-right:3px solid var(--blue-mid)}
.btn.light{border-right-color:#fff}

/* header */
.topbar{left:0;top:0;width:1200px;height:9px;background:var(--navy)}
.phone-pill{left:928px;top:0;width:272px;height:27px;background:var(--navy);border-bottom-left-radius:20px;display:flex;align-items:center;padding-left:34px;color:#fff;font-size:10px;font-family:"Rajdhani",sans-serif;font-weight:600}
.phone-pill i{width:19px;height:19px;border-radius:50%;background:#f4b400;margin-right:8px;display:inline-block}
.logo{display:flex;align-items:center;gap:8px;font-family:"Rajdhani",sans-serif;font-weight:700;font-size:13px;letter-spacing:1px;line-height:1.05;text-transform:uppercase}
.logo .sq{width:26px;height:26px;background:var(--red)}
.nav{top:41px;font-family:"Rajdhani",sans-serif;font-weight:700;font-size:11px;color:var(--ink)}
.nav.on{color:var(--red)}

/* hero */
.hero{left:0;top:69px;width:1200px;height:467px}
.hero-kicker{left:128px;top:214px;color:#fff;font-family:"Rajdhani",sans-serif;font-weight:600;font-size:20px;letter-spacing:.5px}
.hero-title{left:128px;top:234px;color:#fff;font-size:45px;line-height:47px}
.pager{top:465px;color:#fff;font-family:"Rajdhani",sans-serif;font-size:9px;font-weight:700}

/* welcome */
.welcome-back{left:173px;top:635px;width:379px;height:363px;background:var(--peach);border-radius:22px}
.welcome-img{left:130px;top:602px;width:379px;height:364px;border-radius:22px;background:linear-gradient(180deg,#d9e9f5 0%,#c5d5e0 45%,#6b6a5c 75%,#2c2a26 100%)}
.welcome-kicker{left:610px;top:638px;font-size:17px;color:var(--ink);display:flex;align-items:center;width:460px}
.welcome-kicker span{flex:1;height:1px;background:var(--blue-light);margin-left:10px}
.welcome-title{left:610px;top:662px;font-size:44px;line-height:47px}
.welcome-text{left:610px;top:784px;width:462px;font-size:13.5px;line-height:20px;color:var(--ink)}

/* why */
.why{left:0;top:1058px;width:1200px;height:473px;background:var(--blue-pale)}
.sec-title{width:1200px;text-align:center;font-size:43px}
.why-item h3{font-family:"Rajdhani",sans-serif;font-weight:700;font-size:17px;line-height:24px;color:var(--ink);text-transform:uppercase}
.why-item p{font-size:11.5px;line-height:18px;color:var(--ink);width:300px;margin-top:3px}
.why-tile{width:139px;height:137px}
.why-tile.blue{background:linear-gradient(135deg,#0b54b8,#2f8be0)}
.why-tile.green{background:linear-gradient(135deg,#63b80a,#82ff00)}
.why-tile.orange{background:linear-gradient(135deg,#ee7325,#f4a064)}
.why-tile.red{background:linear-gradient(135deg,#e23d36,#f06060)}

/* services */
.sec-sub{width:1200px;text-align:center;font-size:13px;color:var(--ink)}
.card{top:1684px;width:300px;height:294px;background:#fff;border-radius:18px;box-shadow:0 4px 16px rgba(0,0,0,.08);overflow:hidden;text-align:center}
.card .ph{height:150px}
.card h3{font-family:"Rajdhani",sans-serif;font-weight:700;font-size:15px;margin-top:19px;color:var(--ink)}
.card p{font-size:11.5px;line-height:17.5px;padding:0 26px;margin-top:8px;color:var(--ink)}
.card .more{font-size:10px;color:var(--red);text-transform:uppercase;margin-top:11px;display:block}

/* contact */
.contact{left:0;top:2111px;width:1200px;height:391px;background:linear-gradient(135deg,#0c2a45 0%,#1a4468 50%,#0e2c49 100%)}
.contact-title{color:#fff}
.contact-sub{color:#fff}
.field{background:#fff;font-size:10px;color:#333;padding:13px 14px}
.submit{background:var(--red);color:#fff;font-size:10px;display:flex;align-items:center;justify-content:center}

/* projects */
.tile{overflow:hidden}
.tile-hover{background:rgba(235,61,31,.85);display:flex;align-items:center;justify-content:center}
.tile-hover span{position:absolute;inset:8px;border:1px solid rgba(255,255,255,.7)}
.tile-hover b{font-family:"Rajdhani",sans-serif;font-size:15px;color:#fff;text-transform:uppercase;letter-spacing:.5px}

/* footer */
.footer{left:0;top:3076px;width:1200px;height:331px;background:var(--footer);color:#e6e6e6}
.foot-h{font-family:"Rajdhani",sans-serif;font-weight:700;font-size:15px;color:#fff;text-transform:uppercase}
.foot-h em{font-style:normal;color:var(--red)}
.foot-link{font-size:11.5px;color:#ddd;width:96px;border-bottom:1px solid #333;padding-bottom:7px}
.foot-contact{display:flex;align-items:flex-start;gap:10px;font-size:11.5px;line-height:15px;color:#ddd;width:210px}
.foot-contact i{width:24px;height:24px;border-radius:50%;background:#2e2e2e;flex:none;display:flex;align-items:center;justify-content:center}
.social{width:23px;height:23px;border:1px solid #fff;background:#fff}
.social.fb{background:var(--blue);border-color:var(--blue)}
</style>
</head>
<body>

<!-- header -->
<div class="abs topbar"></div>
<div class="abs phone-pill"><i></i>+1 (555) 420 7310</div>
<div class="abs logo" style="left:130px;top:18px;color:var(--ink)"><div class="sq"></div><div>Oak Ledger<br><span style="font-size:9px;letter-spacing:2px">Construction</span></div></div>
<div class="abs nav on" style="left:684px">HOME</div>
<div class="abs nav" style="left:750px">ABOUT US</div>
<div class="abs nav" style="left:839px">SERVICES</div>
<div class="abs nav" style="left:926px">PROJECTS</div>
<div class="abs nav" style="left:1016px">CONTACT US</div>

<!-- hero -->
<svg class="abs hero" viewBox="0 0 1200 467">
  <defs>
    <linearGradient id="heroBlue" x1="0" y1="0" x2="1" y2="1">
      <stop offset="0" stop-color="#1f3f94"/><stop offset="1" stop-color="#2a63c6"/>
    </linearGradient>
    <linearGradient id="heroPhoto" x1="0" y1="0" x2="1" y2="1">
      <stop offset="0" stop-color="#3a3f4a"/><stop offset=".5" stop-color="#5c6a80"/><stop offset="1" stop-color="#8aa4c6"/>
    </linearGradient>
  </defs>
  <rect width="1200" height="467" fill="url(#heroBlue)"/>
  <polygon points="715,0 1200,0 1200,467 463,467" fill="url(#heroPhoto)" role="img" aria-label="Modern brick and glass building viewed from below against a blue sky"/>
  <polygon points="0,378 600,467 0,467" fill="#fff"/>
  <polygon points="598,467 1200,370 1200,467" fill="#fff"/>
  <polygon points="598,460 1200,360 1200,372 604,469" fill="var(--red)"/>
  <line x1="440" y1="401" x2="562" y2="401" stroke="#7a93c9" stroke-width="1"/>
  <line x1="638" y1="401" x2="770" y2="401" stroke="#7a93c9" stroke-width="1"/>
  <circle cx="578" cy="401" r="16" fill="none" stroke="#9fb3dc"/>
  <circle cx="622" cy="401" r="16" fill="none" stroke="#9fb3dc"/>
  <path d="M581 394 l-6 7 6 7 M619 394 l6 7 -6 7" fill="none" stroke="#fff" stroke-width="1.2"/>
</svg>
<div class="abs pager" style="left:413px">PREV</div>
<div class="abs pager" style="left:766px">NEXT</div>
<div class="abs hero-kicker">WE HAVE A PASSION IN</div>
<div class="abs hero-title serif" style="color:#fff">Creating New<br>and Unique Spaces</div>
<div class="btn light" style="left:127px;top:359px;width:96px;height:31px">Read More</div>

<!-- welcome -->
<div class="abs welcome-back"></div>
<div class="abs welcome-img" role="img" aria-label="Tower cranes over a high-rise under construction"></div>
<div class="abs welcome-kicker">Welcome To<span></span></div>
<div class="abs welcome-title serif">Oak Ledger<br>Construction</div>
<p class="abs welcome-text">On the other hand, we denounce with righteous indignation and dislike men who are so beguiled and demoralized by the charms of pleasure of the moment, so blinded by desire that they cannot foresee the pain and trouble that are bound to ensue and equal blame belongs...</p>
<div class="btn" style="left:609px;top:893px;width:97px;height:29px">Read More</div>

<!-- why choose us -->
<div class="abs why"></div>
<div class="abs sec-title serif" style="left:0;top:1096px">Why Choose Us</div>

<div class="abs why-item" style="left:130px;top:1201px"><h3>To Take A<br>Trivial Example</h3><p>But I must explain to you how all this mistaken idea of denouncing pleasure and praising</p></div>
<div class="abs why-item" style="left:770px;top:1201px"><h3>Him Some<br>Great Pleasure</h3><p>But I must explain to you how all this mistaken idea of denouncing pleasure and praising</p></div>
<div class="abs why-item" style="left:130px;top:1367px"><h3>Accusamus Et Iusto<br>Dignissimos</h3><p>But I must explain to you how all this mistaken idea of denouncing pleasure and praising</p></div>
<div class="abs why-item" style="left:770px;top:1367px"><h3>Cum Soluta<br>Eligendi Optio Cumque</h3><p>But I must explain to you how all this mistaken idea of denouncing pleasure and praising</p></div>

<div class="abs why-tile blue" style="left:447px;top:1180px" role="img" aria-label="Blue feature tile with a safety helmet icon"></div>
<div class="abs why-tile green" style="left:614px;top:1180px" role="img" aria-label="Green feature tile with a house and gear icon"></div>
<div class="abs why-tile orange" style="left:447px;top:1346px" role="img" aria-label="Orange feature tile with a crane load icon"></div>
<div class="abs why-tile red" style="left:614px;top:1346px" role="img" aria-label="Red feature tile with a gear and wrench icon"></div>

<!-- services -->
<div class="abs sec-title serif" style="left:0;top:1578px">Our Services</div>
<div class="abs sec-sub" style="left:0;top:1632px">At vero eos et accusamus et iusto odio dignissimos ducimus</div>

<div class="abs card" style="left:130px">
  <div class="ph" role="img" aria-label="Interior under renovation with covered staircase and scaffolding" style="background:linear-gradient(135deg,#8d7a5c,#d8c8a8 55%,#a89272)"></div>
  <h3>RESIDENTIAL</h3>
  <p>On the other hand, we denounce righteous indignation and dislike men who are so beguiled.</p>
  <span class="more">Read More</span>
</div>
<div class="abs card" style="left:450px">
  <div class="ph" role="img" aria-label="Open commercial floor being fitted out with a ladder" style="background:linear-gradient(135deg,#c9cfd4,#f1eee6 55%,#b8a48a)"></div>
  <h3>COMMERCIAL</h3>
  <p>On the other hand, we denounce righteous indignation and dislike men who are so beguiled.</p>
  <span class="more">Read More</span>
</div>
<div class="abs card" style="left:770px">
  <div class="ph" role="img" aria-label="Remodeled loft interior with dark mezzanine" style="background:linear-gradient(135deg,#9b9b9b,#3b3b3b 55%,#b99d72)"></div>
  <h3>REMODEL</h3>
  <p>On the other hand, we denounce righteous indignation and dislike men who are so beguiled.</p>
  <span class="more">Read More</span>
</div>
<div class="btn" style="left:542px;top:2021px;width:116px;height:28px">View All Services</div>

<!-- contact -->
<div class="abs contact" role="img" aria-label="Dark blue view of glass tower steel frame"></div>
<div class="abs sec-title serif contact-title" style="left:0;top:2184px">Contact Us</div>
<div class="abs sec-sub contact-sub" style="left:0;top:2240px">But I must explain to you how all this mistaken idea of denouncing pleasure</div>
<div class="abs field" style="left:274px;top:2281px;width:323px;height:39px">Name:</div>
<div class="abs field" style="left:274px;top:2328px;width:323px;height:40px">Email:</div>
<div class="abs field" style="left:274px;top:2376px;width:323px;height:40px">Phone:</div>
<div class="abs field" style="left:603px;top:2281px;width:323px;height:87px">Comments:</div>
<div class="abs submit" style="left:603px;top:2376px;width:323px;height:40px">Submit</div>

<!-- projects -->
<div class="abs sec-title serif" style="left:0;top:2551px">Recent Projects</div>
<div class="abs tile" style="left:130px;top:2638px;width:300px;height:181px;background:linear-gradient(135deg,#8a6a4a,#c9a87a)" role="img" aria-label="Living room interior">
  <div class="tile-hover abs" style="inset:0"><span></span><b>Fibunus Lorem</b></div>
</div>
<div class="abs tile" style="left:130px;top:2834px;width:300px;height:181px;background:linear-gradient(135deg,#e9e7e2,#b9b2a6 60%,#7a6a58)" role="img" aria-label="Bright office with desk and city view"></div>
<div class="abs tile" style="left:450px;top:2638px;width:300px;height:377px;background:linear-gradient(180deg,#d9cfbe,#a47a52 60%,#6a4a30)" role="img" aria-label="Wooden staircase in a two-storey hallway"></div>
<div class="abs tile" style="left:770px;top:2638px;width:300px;height:181px;background:linear-gradient(135deg,#8e8c88,#dcd8d0 55%,#6f6a62)" role="img" aria-label="Modern bedroom with built-in shelves"></div>
<div class="abs tile" style="left:770px;top:2834px;width:300px;height:181px;background:linear-gradient(135deg,#e4e4e0,#4a5060 55%,#a7784a)" role="img" aria-label="Study with tall bookshelf and wooden floor"></div>

<!-- footer -->
<div class="abs footer"></div>
<div class="abs logo" style="left:130px;top:3160px;color:#fff"><div class="sq"></div><div>Oak Ledger<br><span style="font-size:9px;letter-spacing:2px">Construction</span></div></div>
<div class="abs social fb" style="left:130px;top:3233px"></div>
<div class="abs social" style="left:165px;top:3233px"></div>
<div class="abs social" style="left:199px;top:3233px"></div>
<div class="abs social" style="left:233px;top:3233px"></div>

<div class="abs foot-h" style="left:349px;top:3121px"><em>Quick</em> Links</div>
<div class="abs foot-link" style="left:349px;top:3153px">Home</div>
<div class="abs foot-link" style="left:349px;top:3180px">About Us</div>
<div class="abs foot-link" style="left:349px;top:3206px">Services</div>
<div class="abs foot-link" style="left:349px;top:3233px">Projects</div>
<div class="abs foot-link" style="left:349px;top:3259px;border:0">Contact Us</div>

<div class="abs foot-h" style="left:562px;top:3121px"><em>Contact</em> Us</div>
<div class="abs foot-contact" style="left:565px;top:3155px"><i><svg width="10" height="12" viewBox="0 0 10 12"><path d="M5 0a4 4 0 0 1 4 4c0 3-4 8-4 8S1 7 1 4a4 4 0 0 1 4-4z" fill="#fff"/><circle cx="5" cy="4" r="1.5" fill="#2e2e2e"/></svg></i><span>15k lorem ipsum dolar site<br>Arizona25LP USA</span></div>
<div class="abs" style="left:565px;top:3203px;width:208px;height:1px;background:#333"></div>
<div class="abs foot-contact" style="left:565px;top:3216px;align-items:center"><i><svg width="10" height="10" viewBox="0 0 10 10"><path d="M2 0l2 2-1 2c1 1 2 2 3 3l2-1 2 2-1.5 2C4 10 0 6 0 1.5z" fill="#fff"/></svg></i><span>+1 (555) 420 7310</span></div>
<div class="abs" style="left:565px;top:3255px;width:208px;height:1px;background:#333"></div>
<div class="abs foot-contact" style="left:565px;top:3269px;align-items:center;width:260px"><i><svg width="11" height="8" viewBox="0 0 11 8"><rect width="11" height="8" fill="#fff"/><path d="M0 0l5.5 4.5L11 0" fill="none" stroke="#2e2e2e"/></svg></i><span>info@oakledgerbuild.com</span></div>

<div class="abs foot-h" style="left:849px;top:3121px"><em>News</em>letter</div>
<div class="abs field" style="left:849px;top:3155px;width:221px;height:35px;font-size:9.5px;padding:11px 11px">Enter Your Email:</div>
<div class="abs submit" style="left:849px;top:3196px;width:221px;height:33px;font-family:'Rajdhani',sans-serif;font-weight:700;font-size:11px">SUBSCRIBE</div>

<div class="abs" style="left:130px;top:3318px;width:940px;height:1px;background:#2c2c2c"></div>
<div class="abs" style="left:0;top:3347px;width:1200px;text-align:center;font-size:10.5px;color:#ddd">Copyright © 2022 <span style="color:var(--red)">Oak Ledger Construction</span>. All Rights Reserved.</div>

</body>
</html>
```